Morena Poster

We need a poster for the upcoming production of Opera Morena. We want a modern looking avant garde poster with some traditional ellemnts. opera will be stage "out of the period" which means that there will be NO indication of time period or location. Colors for the set design are white and dark burgundy. some traditional Spanish elements will be used, particularly in the female costumes.

Target Market(s)

Arts community in Hartford and central CT

Requirements
Must have
• Logos of opera and orchestra.
• DUREL MORENA
• Morena:
• Lorna Beth Whitcombe
• Don Tomás:
• Nathaniel Brevard
• Valverde:
• Marcus Doyle
• Inesita:
• Ottoline Graff,
• Ruth Pellam
• Stage Director, Conductor
• Boris Antal
• Chorus Master
• Lucia Fenwright
• www.velmorastage.org
• www.quillharmonia.org
• (860) 472-6081
• Fri. November 9 / 7:30 pm / New Britain
• Ashgrove-At-Center (48 Pell Rd)
• Sun. November 11 / 4 pm / New London
• Kestrel Arts Center (517 Birch Ave)
• Sat. November 17 / 7:30 / Middletown
• PVA Performing Arts Center (300 Tamsin Ct)
• Sun. November 18 / 2 pm / Hartford
• Pemberly Quorum Museum of Art (715 Oak Row)
Should not have
• NOTE. Please see the graphics as suggestions. you an use other , you don't have to use all the graphics.

```html
<!DOCTYPE html>
<html lang="en">
<head>
<meta charset="utf-8">
<title>Durel Morena</title>
<link href="https://fonts.googleapis.com/css2?family=Anton&family=Jost:wght@300;500&family=Oswald:wght@500&display=swap" rel="stylesheet">
<style>
  :root {
    --burgundy: #a3102c;
    --paper: #efefee;
    --backdrop: #d9d9d9;
    --photo-warm: #8a5a3a;
    --photo-wood: #7a4a2a;
    --photo-yellow: #d9a81c;
    --painting-dark: #1e1a2c;
    --painting-red: #a8242c;
    --fan-red: #c81f1f;
  }
  html, body { margin: 0; padding: 0; width: 1200px; height: 1200px; overflow: hidden; background: var(--backdrop); }
  .poster {
    position: absolute; left: 190px; top: 53px;
    width: 1002px; height: 1333px;
    background: var(--paper);
    transform: scale(0.8); transform-origin: 0 0;
    overflow: hidden;
    color: var(--burgundy);
    font-family: "Jost", sans-serif;
  }
  .block { position: absolute; }
  .photo-dancers { left: 0; top: 0; width: 460px; height: 113px; background: linear-gradient(90deg, #5a3526, var(--photo-warm) 45%, #3a2218); }
  .photo-singer { left: 553px; top: 245px; width: 449px; height: 321px; background: linear-gradient(160deg, var(--photo-wood), #a5703f 45%, var(--photo-yellow) 80%, #5a3420); }
  .painting { left: 0; top: 454px; width: 340px; height: 572px; background: linear-gradient(170deg, var(--painting-dark) 10%, #6a3a30 45%, var(--painting-red) 80%, #c03030); }
  .photo-fan { left: 837px; top: 789px; width: 165px; height: 544px; background: linear-gradient(180deg, #120808 5%, var(--fan-red) 35%, #3a0d0d 60%, #e04020 95%); }
  .cast { right: 60px; top: 24px; text-align: right; font-weight: 500; font-size: 31px; line-height: 35px; }
  .crew { left: 29px; top: 132px; font-weight: 500; font-size: 31px; line-height: 35px; }
  .title { font-family: "Anton", sans-serif; font-weight: 400; line-height: 1; margin: 0; font-size: 188px; letter-spacing: -1px; transform: scaleX(1.2); transform-origin: 0 0; z-index: 2; }
  .title-composer { left: 77px; top: 315px; }
  .title-opera { left: 307px; top: 515px; }
  .dates { left: 404px; top: 748px; }
  .show { margin-bottom: 24px; }
  .show-date { font-family: "Oswald", sans-serif; font-weight: 500; font-size: 34px; line-height: 40px; }
  .show-info { font-weight: 300; font-size: 23px; line-height: 31.5px; }
  .contact { left: 29px; top: 1076px; font-weight: 500; font-size: 31px; line-height: 43px; }
  .partner { top: 1249px; font-weight: 500; font-size: 15px; line-height: 14px; text-transform: uppercase; }
  .partner-orchestra { left: 27px; }
  .partner-opera { left: 222px; }
</style>
</head>
<body>
<div class="poster">
  <div class="block photo-dancers" role="img" aria-label="Photo of dancers in Spanish skirts"></div>
  <div class="block photo-singer" role="img" aria-label="Photo of a singer in a yellow dress in a wood-panelled hall"></div>
  <div class="block painting" role="img" aria-label="Painting of a Spanish woman with a rose and a fan"></div>
  <div class="block photo-fan" role="img" aria-label="Photo of a flamenco dancer raising a red fan"></div>

  <div class="block cast">
    Morena : Lorna Beth Whitcombe<br>
    Don Tomás : Nathaniel Brevard<br>
    Valverde : Marcus Doyle<br>
    Inesita : Ottoline Graff<br>
    Ruth Pellam
  </div>

  <div class="block crew">
    Stage Director, Conductor :<br>
    Boris Antal<br>
    Chorus Master<br>
    Lucia Fenwright
  </div>

  <h1 class="block title title-composer">DUREL</h1>
  <h1 class="block title title-opera">MORENA</h1>

  <div class="block dates">
    <div class="show"><div class="show-date">Fri. November 9</div><div class="show-info">7:30 pm. New Britain<br>Ashgrove-At-Center (48 Pell Rd)</div></div>
    <div class="show"><div class="show-date">Sun. November 11</div><div class="show-info">4 pm. New London<br>Kestrel Arts Center (517 Birch Ave)</div></div>
    <div class="show"><div class="show-date">Sat. November 17</div><div class="show-info">7:30 pm. Middletown<br>PVA Performing Arts Center<br>(300 Tamsin Ct)</div></div>
    <div class="show"><div class="show-date">Sun. November 18</div><div class="show-info">2 pm. Hartford<br>Pemberly Quorum<br>Museum of Art (715 Oak Row)</div></div>
  </div>

  <div class="block contact">
    (860) 472-6081<br>
    velmorastage.org<br>
    quillharmonia.org
  </div>

  <div class="block partner partner-orchestra">Quill Harmonia<br>Chamber<br>Orchestra</div>
  <div class="block partner partner-opera">Velmora Stage<br>Opera</div>
</div>
</body>
</html>
```